Podiatry (services) Business Card

I need a business design for a New Podiatry Service.
the Podiatry services will include all aspects of podiatry including;
general podiatry for all ages
corns and callus treatment
Ingrown toenails & nail surgery
Forefoot, arch and heel pain
Gait analysis
Sports Podiatry and Orthotics
Paediatric Assessments
Diabetes Foot Assessment

I would like the back of the card to have space for next appointment day and time.

I would like a nice design that is simple yet catchy. I don't like cluttered business cards. I like things to be simple yet stand out because of the finer details.

I like the colours blue and white but I'm open to other designs that have different colours.

Kestrel Podiatry (Business name)

Leisel Marrow - Podiatrist
M.Pod.P., B.Hlth. Sci, MQFotA

Address: 58 Tolbrook Rd, Hallow Park Vic, 3190
Phone: (03) 9564 2718
Fax: (03) 9432 6581

```html
<!DOCTYPE html>
<html lang="en">
<head>
<meta charset="utf-8">
<title>Kestrel Podiatry – Business Card</title>
<link href="https://fonts.googleapis.com/css2?family=Questrial&family=EB+Garamond&family=Open+Sans:wght@400;700&display=swap" rel="stylesheet">
<style>
  :root{
    --page:#bcbdbf;
    --blue:#1a9ad6;
    --blue-deep:#2a7bc0;
    --blue-bright:#00aae2;
    --blue-pale:#bfe3f4;
    --ink:#4a4a4a;
    --grey:#7d7d7d;
    --white:#ffffff;
  }
  *{box-sizing:border-box;margin:0;padding:0}
  html,body{width:1200px;height:1200px;overflow:hidden}
  body{background:var(--page);font-family:"Open Sans",Arial,sans-serif;position:relative}
  .card{position:absolute;left:160px;width:880px;height:538px;overflow:hidden;
        box-shadow:0 6px 18px rgba(0,0,0,.18);background:var(--white)}
  .card--back{top:46px;background:linear-gradient(135deg,#9fdcf2 0%,#d4eef9 38%,#ffffff 72%)}
  .card--front{top:620px;background:linear-gradient(90deg,var(--blue-pale) 30%,#e9f6fc 55%,#ffffff 72%)}

  /* front */
  .brand-visual{position:absolute;left:0;top:0;width:340px;height:100%;
        background:linear-gradient(180deg,var(--blue-bright) 0%,#1592d4 50%,var(--blue-deep) 100%)}
  .brand-name{position:absolute;right:60px;top:90px;text-align:right;font-weight:400;
        font-family:"Questrial",sans-serif;color:var(--blue);font-size:88px;line-height:.95;letter-spacing:1px}
  .contact{position:absolute;right:60px;bottom:44px;text-align:right;color:var(--ink)}
  .contact__name{font-family:"EB Garamond",serif;color:var(--blue);font-size:42px;line-height:1}
  .contact__role{font-size:22px;color:var(--ink);margin-left:12px}
  .contact__quals{font-size:21px;margin:6px 0 18px}
  .contact__line{font-size:21px;line-height:1.55}
  .contact__line b{font-weight:700}

  /* back */
  .appt-title{position:absolute;right:60px;top:46px;font-family:"EB Garamond",serif;font-weight:400;
        color:var(--blue);font-size:44px}
  .appt-rows{position:absolute;left:300px;right:60px;top:130px}
  .appt-row{display:flex;align-items:flex-end;gap:10px;font-size:20px;color:var(--ink);margin-bottom:26px}
  .appt-row .dots{flex:1;border-bottom:2px dotted var(--grey);height:1px;margin-bottom:6px}
  .services{position:absolute;left:40px;right:40px;bottom:40px;text-align:center;color:var(--grey);font-size:19px;line-height:1.5}
  .services__head{font-weight:700;color:var(--ink);margin-bottom:4px}
</style>
</head>
<body>
  <section class="card card--back" aria-label="Card back">
    <h2 class="appt-title">Next Appointment</h2>
    <div class="appt-rows">
      <div class="appt-row">Day<span class="dots"></span>Time<span class="dots"></span></div>
      <div class="appt-row">Day<span class="dots"></span>Time<span class="dots"></span></div>
      <div class="appt-row">Day<span class="dots"></span>Time<span class="dots"></span></div>
    </div>
    <div class="services">
      <p class="services__head">The Podiatry services will include all aspects of podiatry including</p>
      <p>General podiatry for all ages | Corns and callus treatment</p>
      <p>Ingrown toenails &amp; nail surgery | Forefoot, arch and heel pain</p>
      <p>Gait analysis | Sports Podiatry and Orthotics</p>
      <p>Paediatric Assessments | Diabetes Foot Assessment</p>
    </div>
  </section>

  <section class="card card--front" aria-label="Card front">
    <div class="brand-visual" role="img" aria-label="Blue foot illustration area"></div>
    <h1 class="brand-name">Kestrel<br>Podiatry</h1>
    <div class="contact">
      <p><span class="contact__name">Leisel Marrow</span><span class="contact__role">Podiatrist</span></p>
      <p class="contact__quals">M.Pod.P., B.Hlth. Sci, MQFotA</p>
      <p class="contact__line"><b>T.</b> (03) 9564 2718 <b>F.</b> (03) 9432 6581</p>
      <p class="contact__line">58 Tolbrook Rd, Hallow Park Vic, 3190</p>
    </div>
  </section>
</body>
</html>
```